Business card design needed with logo

My business is called KVM Solutions & it is targeted towards mobile equipment maintenance in the Mining and civil industry. My work involves maintenance planning and maintenance management plus also supply tradespeople on a labour hire basis. We can provide from basic shut-down machine rebuild plans to complete rebuild services supply plans and labour to anywhere in Australia. I would like to use the colours Black, Red and Grey, I had done a desgin as attached but doesn't really explain what we do and gears don't embroider well onto shirts.
Updates

I also wanted to see the something replace the gears maybe just making the KVM lettering look a bit different or put together differently 

Hello I have extended the deadline by a few extra days as I would like to update details on the front of card, details below & can be put which ever way looks good;

Liam Fenwick
Director
0417263958
KVM@mailnest.com.au
www.kvmsolutions-demo.com.au

On the back of the card I would like to have the below printed;

Capable of providing, but not limited to, across Australia:
- Contract Maintenance Planning.
- Skilled Mobile Maintenance labour hire.
- New machine build specifications. 
- Plant risk assessments and inspections.
- Shut down and rebuild program planning.
- Preventative maintenance tasks, including build of materials lists, creation and review.

Target Market(s)

Contractors and companies that use small and large earthmoving and mining machines

Industry/Entity Type

Business

Contact Information for Business Card

Trading name is KVM Solutions
My name and title is
Liam Fenwick Director
0417 263 958
KVM@mailnest.com.au

Logo Text

KVM

```html
<!DOCTYPE html>
<html lang="en">
<head>
<meta charset="utf-8">
<title>KVM Solutions – Business Card</title>
<link rel="stylesheet" href="https://fonts.googleapis.com/css2?family=Orbitron:wght@500;700;800&display=swap">
<style>
  :root {
    --backdrop: #2a2a2a;
    --red-deep: #a8141a;
    --red-bright: #d9221f;
    --card-black: #0c0c0c;
    --white: #ffffff;
    --grey: #d6d6d6;
    --accent-red: #e0241f;
  }
  * { margin: 0; padding: 0; box-sizing: border-box; }
  html, body {
    width: 1200px;
    height: 900px;
    overflow: hidden;
    background: var(--backdrop);
    font-family: "Orbitron", sans-serif;
  }
  .canvas {
    position: relative;
    width: 1200px;
    height: 900px;
  }
  .card {
    position: absolute;
    top: 310px;
    width: 480px;
    height: 280px;
    border-radius: 26px;
    overflow: hidden;
    box-shadow: 0 18px 36px rgba(0,0,0,0.5);
  }
  .card--front {
    left: 70px;
    background: linear-gradient(120deg, var(--red-deep) 0%, var(--red-bright) 100%);
    display: flex;
    align-items: center;
    justify-content: center;
  }
  .card--back {
    left: 650px;
    background: var(--card-black);
  }
  .wordmark {
    display: flex;
    align-items: center;
    gap: 14px;
  }
  .wordmark__square {
    width: 26px;
    height: 26px;
    background: var(--white);
    flex: none;
  }
  .brand-name {
    font-weight: 800;
    font-size: 34px;
    letter-spacing: 1px;
    text-transform: uppercase;
    color: var(--white);
    white-space: nowrap;
  }
  .card--back .wordmark {
    position: absolute;
    top: 128px;
    right: 44px;
    gap: 10px;
  }
  .card--back .wordmark__square {
    width: 18px;
    height: 18px;
    background: var(--accent-red);
  }
  .card--back .brand-name {
    font-size: 24px;
    color: var(--accent-red);
  }
  .contact {
    position: absolute;
    right: 44px;
    bottom: 38px;
    text-align: right;
    color: var(--white);
  }
  .contact__name {
    font-weight: 700;
    font-size: 17px;
    letter-spacing: 1px;
  }
  .contact__title {
    font-weight: 500;
    font-size: 11px;
    margin-top: 3px;
    color: var(--grey);
  }
  .contact__details {
    font-weight: 500;
    font-size: 12px;
    margin-top: 12px;
    letter-spacing: 0.5px;
    white-space: nowrap;
  }
  .contact__divider {
    color: var(--accent-red);
    margin: 0 5px;
  }
</style>
</head>
<body>
  <main class="canvas">
    <section class="card card--front" aria-label="Card front">
      <div class="wordmark">
        <span class="wordmark__square" aria-hidden="true"></span>
        <span class="brand-name">KVM Solutions</span>
      </div>
    </section>
    <section class="card card--back" aria-label="Card back">
      <div class="wordmark">
        <span class="wordmark__square" aria-hidden="true"></span>
        <span class="brand-name">KVM Solutions</span>
      </div>
      <div class="contact">
        <p class="contact__name">LIAM FENWICK</p>
        <p class="contact__title">DIRECTOR</p>
        <p class="contact__details">0417 263 958<span class="contact__divider">|</span>KVM@MAILNEST.COM.AU</p>
      </div>
    </section>
  </main>
</body>
</html>
```